Real Estate Email Signature

I need a professional looking real estate email signature with my picture, logo, and Name, Real Estate Broker/Realtor, and Top of Harbeck logo

```html
<!DOCTYPE html>
<html lang="en">
<head>
<meta charset="utf-8">
<title>Sam Ridley — Email Signature</title>
<link href="https://fonts.googleapis.com/css2?family=Barlow:wght@400;500;700&display=swap" rel="stylesheet">
<style>
  :root {
    --brand-blue: #1f5a7c;
    --brand-navy: #2a3481;
    --text-dark: #3a3f44;
    --text-muted: #6a7077;
    --photo-light: #d9dde1;
    --photo-dark: #7d858d;
    --skyline-tint: #eef0f2;
    --white: #ffffff;
  }
  html, body {
    margin: 0;
    padding: 0;
    overflow: hidden;
    background: var(--white);
  }
  .signature {
    position: relative;
    width: 1200px;
    height: 300px;
    overflow: hidden;
    background: var(--white);
    font-family: "Barlow", Arial, sans-serif;
  }
  .skyline {
    position: absolute;
    left: 560px;
    top: 20px;
    width: 260px;
    height: 224px;
    background: linear-gradient(180deg, rgba(238,240,242,0) 0%, var(--skyline-tint) 100%);
  }
  .portrait {
    position: absolute;
    left: 34px;
    top: 0;
  }
  .brand-mark {
    position: absolute;
    left: 30px;
    top: 10px;
    width: 70px;
    height: 70px;
    border-radius: 50%;
    background: var(--brand-blue);
    color: var(--white);
    display: flex;
    align-items: center;
    justify-content: center;
    font-weight: 700;
    font-size: 26px;
    letter-spacing: 1px;
  }
  .agent-name {
    position: absolute;
    left: 326px;
    top: 68px;
    margin: 0;
    font-size: 66px;
    line-height: 1;
    font-weight: 700;
    letter-spacing: 2px;
    color: var(--brand-blue);
  }
  .agent-title {
    position: absolute;
    left: 328px;
    top: 150px;
    margin: 0;
    font-size: 26px;
    font-weight: 400;
    color: var(--text-muted);
  }
  .contact {
    position: absolute;
    left: 798px;
    top: 62px;
  }
  .contact-row {
    display: flex;
    align-items: center;
    gap: 26px;
    margin-bottom: 22px;
  }
  .contact-icon {
    width: 44px;
    height: 44px;
    border-radius: 50%;
    background: var(--brand-blue);
    display: flex;
    align-items: center;
    justify-content: center;
    flex-shrink: 0;
  }
  .contact-text {
    font-size: 27px;
    line-height: 1.2;
    color: var(--text-dark);
  }
  .contact-phone {
    font-weight: 500;
  }
  .footer-band {
    position: absolute;
    left: 0;
    bottom: 0;
    width: 1200px;
    height: 56px;
    background: var(--brand-navy);
  }
  .award {
    position: absolute;
    left: 796px;
    top: 14px;
    display: flex;
    align-items: center;
    gap: 10px;
    color: var(--white);
    font-weight: 700;
    font-size: 19px;
    letter-spacing: 1px;
  }
  .award-square {
    width: 20px;
    height: 20px;
    background: var(--white);
  }
</style>
</head>
<body>
  <div class="signature">
    <div class="skyline" role="img" aria-label="Faint city skyline backdrop"></div>

    <svg class="portrait" width="270" height="246" viewBox="0 0 270 246" role="img" aria-label="Portrait photo of the agent">
      <defs>
        <linearGradient id="portraitFill" x1="0" y1="0" x2="0" y2="1">
          <stop offset="0" stop-color="var(--photo-light)"/>
          <stop offset="1" stop-color="var(--photo-dark)"/>
        </linearGradient>
      </defs>
      <path d="M48 0 H222 Q232 0 236 10 L268 112 Q271 122 268 132 L236 234 Q232 244 222 244 H48 Q38 244 34 234 L2 132 Q-1 122 2 112 L34 10 Q38 0 48 0 Z" fill="url(#portraitFill)"/>
    </svg>

    <div class="brand-mark">NH</div>

    <h1 class="agent-name">SAM RIDLEY</h1>
    <p class="agent-title">Director</p>

    <div class="contact">
      <div class="contact-row">
        <span class="contact-icon">
          <svg width="22" height="26" viewBox="0 0 22 26" aria-hidden="true">
            <path d="M11 1C5.5 1 1.5 5.2 1.5 10.3 1.5 17 11 25 11 25s9.5-8 9.5-14.7C20.5 5.2 16.5 1 11 1z" fill="var(--white)"/>
            <circle cx="11" cy="10.3" r="3.6" fill="var(--brand-blue)"/>
          </svg>
        </span>
        <span class="contact-text">4820 Willow Bend Court<br>Fairview, IN 46100</span>
      </div>
      <div class="contact-row">
        <span class="contact-icon">
          <svg width="22" height="22" viewBox="0 0 24 24" aria-hidden="true">
            <path d="M6.6 10.8a15.1 15.1 0 006.6 6.6l2.2-2.2c.3-.3.7-.4 1-.2 1.1.4 2.3.6 3.6.6.6 0 1 .4 1 1V20c0 .6-.4 1-1 1A17 17 0 013 4c0-.6.4-1 1-1h3.5c.6 0 1 .4 1 1 0 1.3.2 2.5.6 3.6.1.3 0 .7-.2 1l-2.3 2.2z" fill="var(--white)"/>
          </svg>
        </span>
        <span class="contact-text contact-phone">555-014-2287</span>
      </div>
    </div>

    <div class="footer-band">
      <div class="award">
        <span class="award-square"></span>
        <span>TOP OF HARBECK</span>
      </div>
    </div>
  </div>
</body>
</html>
```